Business Card Design Project - Tall Maple

We are looking for a new business card design. Our company name is Tall Maple Communication Solutions. Our primary function is to provide our clients with communication solutions. These solutions include commercial phone systems and T1 and Fiber Internet lines. Another major part of the business is cabling new buildings with CAT5 cable for both data and phone.

Industry/Entity Type

Communication

Requirements
Must have
• The cards need to be two sided and have some bleeding edge color.
Nice to have
• We are going to upload our current logo BUT we are not married to this logo. If you want to incorporate a re-designed logo with the new business card - please feel free to do so. We are looking for a new bold look that is very colorful yet professional.

```html
<!DOCTYPE html>
<html lang="en">
<head>
<meta charset="utf-8">
<title>Tall Maple Communication Solutions – Business Card</title>
<link rel="stylesheet" href="https://fonts.googleapis.com/css2?family=Questrial&display=swap">
<style>
  :root {
    --backdrop: #7a5335;
    --card: #ffffff;
    --brand-blue: #1f5fa8;
    --ink: #1d2a3a;
    --card-shadow: rgba(0, 0, 0, 0.35);
  }
  html, body {
    margin: 0;
    padding: 0;
    width: 1200px;
    height: 900px;
    overflow: hidden;
    background: var(--backdrop);
  }
  .canvas {
    position: relative;
    width: 1200px;
    height: 900px;
    font-family: "Questrial", "Century Gothic", sans-serif;
    color: var(--ink);
  }
  .card {
    position: absolute;
    top: 284px;
    width: 494px;
    height: 302px;
    background: var(--card);
    box-shadow: 0 4px 14px var(--card-shadow);
    overflow: hidden;
  }
  .card--front { left: 68px; }
  .card--back { left: 642px; }
  .card__art {
    position: absolute;
    inset: 0;
    width: 100%;
    height: 100%;
  }
  .brand {
    position: absolute;
    line-height: 1;
    white-space: nowrap;
  }
  .brand__name {
    display: block;
    font-size: 28px;
    color: var(--brand-blue);
    letter-spacing: 0.2px;
  }
  .brand__tagline {
    display: block;
    margin-top: 4px;
    font-size: 12px;
    color: var(--brand-blue);
    letter-spacing: 0.3px;
  }
  .card--front .brand { left: 22px; top: 118px; }
  .card--back .brand { left: 124px; top: 128px; }
  .contact {
    position: absolute;
    left: 78px;
    top: 172px;
    margin: 0;
    font-style: normal;
    font-size: 12.5px;
    line-height: 16px;
    color: var(--ink);
  }
  .contact__group + .contact__group { margin-top: 16px; }
  .contact span { display: block; }
</style>
</head>
<body>
<main class="canvas">

  <section class="card card--front" aria-label="Business card front">
    <svg class="card__art" viewBox="0 0 494 302">
      <defs>
        <linearGradient id="band-fade" x1="0" y1="0" x2="1" y2="0">
          <stop offset="0" stop-color="#4a8fd0" stop-opacity="0.25"/>
          <stop offset="0.45" stop-color="#4a8fd0" stop-opacity="0.8"/>
          <stop offset="1" stop-color="#1f5fa8"/>
        </linearGradient>
        <linearGradient id="tile-fade" x1="0" y1="0" x2="1" y2="0">
          <stop offset="0" stop-color="#5bb6e6" stop-opacity="0.9"/>
          <stop offset="1" stop-color="#a9d3f0" stop-opacity="0.5"/>
        </linearGradient>
        <radialGradient id="globe-fill" cx="0.4" cy="0.35" r="0.7">
          <stop offset="0" stop-color="#d9ecfa"/>
          <stop offset="0.6" stop-color="#4a8fd0"/>
          <stop offset="1" stop-color="#1f5fa8"/>
        </radialGradient>
      </defs>
      <path class="top-band" d="M0 0 H494 V70 C420 74 330 50 250 34 C170 20 80 22 0 30 Z" fill="url(#band-fade)"/>
      <path class="tile-ribbon" role="img" aria-label="Ribbon of small blue square tiles"
            d="M0 10 C90 8 170 20 250 44 C300 60 340 88 380 104 L376 120 C330 104 290 84 240 66 C160 42 80 40 0 44 Z"
            fill="url(#tile-fade)"/>
      <circle class="globe" role="img" aria-label="Globe showing the Americas" cx="420" cy="92" r="68" fill="url(#globe-fill)"/>
    </svg>

    <div class="brand">
      <span class="brand__name">Tall Maple</span>
      <span class="brand__tagline">COMMUNICATION SOLUTIONS</span>
    </div>

    <address class="contact">
      <div class="contact__group">
        <span>0000 Anyway Road.</span>
        <span>Yourcity, State&nbsp; 00000-0000</span>
      </div>
      <div class="contact__group">
        <span>Phone: 000-000-0000</span>
        <span>www.tallmaple-cs.com</span>
        <span>E-mail: info@tallmaple-cs.com</span>
      </div>
    </address>
  </section>

  <section class="card card--back" aria-label="Business card back">
    <svg class="card__art" viewBox="0 0 494 302">
      <defs>
        <linearGradient id="back-top-fade" x1="0" y1="0" x2="1" y2="0">
          <stop offset="0" stop-color="#a9d3f0" stop-opacity="0.6"/>
          <stop offset="0.5" stop-color="#5bb6e6" stop-opacity="0.9"/>
          <stop offset="1" stop-color="#5bb6e6" stop-opacity="0.4"/>
        </linearGradient>
        <linearGradient id="back-bottom-fade" x1="0" y1="0" x2="1" y2="0">
          <stop offset="0" stop-color="#5bb6e6" stop-opacity="0.4"/>
          <stop offset="0.5" stop-color="#5bb6e6" stop-opacity="0.9"/>
          <stop offset="1" stop-color="#a9d3f0" stop-opacity="0.6"/>
        </linearGradient>
      </defs>
      <path class="tile-ribbon" role="img" aria-label="Ribbon of small blue square tiles"
            d="M38 6 H300 C330 10 350 40 370 66 L356 74 C330 54 300 48 260 46 C180 44 110 46 38 46 Z"
            fill="url(#back-top-fade)"/>
      <path class="tile-ribbon" role="img" aria-label="Ribbon of small blue square tiles"
            d="M120 226 C170 214 210 210 260 214 C330 220 400 234 494 240 V296 H250 C200 290 170 270 130 250 Z"
            fill="url(#back-bottom-fade)"/>
    </svg>

    <div class="brand">
      <span class="brand__name">Tall Maple</span>
      <span class="brand__tagline">COMMUNICATION SOLUTIONS</span>
    </div>
  </section>

</main>
</body>
</html>
```